Business Card Design for Venture Kite

Venture Kite is a pro bono student consultancy service offered by Corvala KTRB to social start ups and enterprises. We provide consulting services with expertise in areas such as Marketing, IT, Business Strategy and Innovation.
I have attached\ the Venture Kite Logo here for your perusal.
Industry/Entity Type
Business
Contact Information for Business Card
Name: Ha Min Park Name: Thomas Leung
Role: Project Leader Role: Vice Project Leader
M:0477203941 M: 0479352806
E: ha-min.park@corvalaktrb.org E: thomas.leung@corvalaktrb.org
W: www.corvalaktrb.org W: www.corvalaktrb.org

```html
<!DOCTYPE html>
<html lang="en">
<head>
<meta charset="utf-8">
<title>Venture Kite Business Card Design</title>
<link rel="stylesheet" href="https://fonts.googleapis.com/css2?family=Fira+Sans+Condensed:wght@700&family=Montserrat:wght@400;500&family=Open+Sans:wght@400&display=swap">
<style>
  :root {
    --page: #ffffff;
    --ink: #111111;
    --black: #000000;
    --orange: #f7941d;
    --trim: #e8474c;
    --white: #ffffff;
  }
  * { box-sizing: border-box; margin: 0; padding: 0; }
  html, body {
    width: 848px;
    height: 1200px;
    overflow: hidden;
    background: var(--page);
  }
  .sheet {
    position: relative;
    width: 848px;
    height: 1200px;
    background: var(--page);
    color: var(--ink);
  }
  .sheet-title {
    position: absolute;
    top: 32px;
    left: 0;
    width: 100%;
    text-align: center;
    font-family: "Open Sans", sans-serif;
    font-size: 14px;
    font-weight: 400;
    letter-spacing: 0.2px;
  }
  .card-front {
    position: absolute;
    left: 242px;
    top: 302px;
    width: 367px;
    height: 222px;
    border: 1px solid var(--trim);
    background: var(--white);
  }
  .accent-bar {
    position: absolute;
    left: 211px;
    width: 131px;
    height: 15px;
  }
  .accent-bar--top { top: -1px; background: var(--orange); }
  .accent-bar--bottom { bottom: -1px; background: var(--black); }
  .brand-name {
    font-family: "Fira Sans Condensed", sans-serif;
    font-weight: 700;
    text-transform: uppercase;
    line-height: 1;
    white-space: nowrap;
  }
  .card-front .brand-name {
    position: absolute;
    left: 211px;
    top: 44px;
    width: 131px;
    text-align: center;
    font-size: 24px;
    color: var(--black);
  }
  .holder {
    position: absolute;
    left: 17px;
    top: 155px;
    font-family: "Montserrat", sans-serif;
  }
  .holder-name { font-size: 13px; font-weight: 500; line-height: 1.2; }
  .holder-role { font-size: 7.5px; font-weight: 400; margin-top: 2px; }
  .contact-list {
    position: absolute;
    left: 212px;
    top: 155px;
    list-style: none;
    font-family: "Montserrat", sans-serif;
    font-size: 8px;
    line-height: 1;
  }
  .contact-list li { margin-bottom: 6px; white-space: nowrap; }
  .contact-list li:last-child { margin-top: 3px; }
  .contact-label { display: inline-block; width: 12px; }
  .card-back {
    position: absolute;
    left: 232px;
    top: 674px;
    width: 386px;
    height: 241px;
    background: var(--black);
  }
  .card-back .brand-name {
    position: absolute;
    left: 0;
    top: 108px;
    width: 100%;
    text-align: center;
    font-size: 27px;
    color: var(--white);
  }
</style>
</head>
<body>
  <main class="sheet">
    <h1 class="sheet-title">VENTURE KITE BUSINESS CARD DESIGN SAMPLE</h1>

    <section class="card-front" aria-label="Business card front">
      <div class="accent-bar accent-bar--top"></div>
      <div class="brand-name">Venture Kite</div>
      <div class="holder">
        <p class="holder-name">Ha Min Park</p>
        <p class="holder-role">Project Leader</p>
      </div>
      <ul class="contact-list">
        <li><span class="contact-label">M:</span>0477203941</li>
        <li><span class="contact-label">E:</span>ha-min.park@corvalaktrb.org</li>
        <li><span class="contact-label">W:</span>www.corvalaktrb.org</li>
      </ul>
      <div class="accent-bar accent-bar--bottom"></div>
    </section>

    <section class="card-back" aria-label="Business card back">
      <div class="brand-name">Venture Kite</div>
    </section>
  </main>
</body>
</html>
```